Voltren Assemblies, Inc. Business Card

Voltren has three operating entities and I'm looking for a standard business card template that can be used for Voltren and the three operating entities that the logo just get swapped out, but has a very similar look and feel. Ultimately if someone had a business card from each, they assume the organizations are related because they all have the same look and feel.
Below are our websites and I will attached the logos for each entity:
https://www.voltrenassemblies-example.com/
https://www.brackwayceramic-example.com/
https://www.omdr-pqsx-example.com/
https://www.tamberlinebreaker-example.com/

Target Market(s)

US Voltren

Industry/Entity Type

US Voltren

Contact Information for Business Card

Normal stuff

```html
<!DOCTYPE html>
<html lang="en">
<head>
<meta charset="utf-8">
<title>Tamberline Breaker – Business Card</title>
<link rel="stylesheet" href="https://fonts.googleapis.com/css2?family=Montserrat:wght@400;500&family=Source+Sans+3:wght@600;700&display=swap">
<style>
  :root {
    --brand-blue: #5a7491;
    --card-white: #f7f7f7;
    --ink: #1f1f1f;
    --page: #a4a4a4;
    --icon-white: #ffffff;
  }
  html, body {
    margin: 0;
    width: 1200px;
    height: 1200px;
    overflow: hidden;
    background: var(--page);
  }
  .stage {
    position: relative;
    width: 1200px;
    height: 1200px;
  }
  .card {
    position: absolute;
    left: 200px;
    width: 800px;
    height: 456px;
    border-radius: 22px;
    background: linear-gradient(135deg, #ffffff 0%, #efefef 100%);
    box-shadow: 0 10px 26px rgba(0,0,0,0.22);
    overflow: hidden;
  }
  .card--front { top: 116px; }
  .card--back { top: 628px; }

  /* front */
  .side-band {
    position: absolute;
    left: 0; top: 0;
    width: 179px; height: 100%;
    background: var(--brand-blue);
  }
  .side-band svg { display: block; }
  .band-name {
    font-family: "Source Sans 3", sans-serif;
    font-weight: 700;
    font-size: 22px;
    letter-spacing: 0.5px;
    fill: var(--icon-white);
  }
  .band-tagline {
    font-family: "Source Sans 3", sans-serif;
    font-weight: 700;
    font-size: 9.5px;
    fill: var(--icon-white);
  }
  .person {
    position: absolute;
    left: 241px;
    top: 80px;
  }
  .person__name {
    margin: 0;
    font-family: "Source Sans 3", sans-serif;
    font-weight: 700;
    font-size: 42px;
    line-height: 1;
    color: var(--brand-blue);
  }
  .person__title {
    margin: 6px 0 0;
    font-family: "Montserrat", sans-serif;
    font-weight: 400;
    font-size: 20px;
    color: var(--ink);
  }
  .contact {
    position: absolute;
    left: 241px;
    display: flex;
    align-items: center;
    gap: 22px;
    font-family: "Montserrat", sans-serif;
    font-size: 20px;
    line-height: 28px;
    color: var(--ink);
  }
  .contact--phone { top: 196px; }
  .contact--web { top: 252px; }
  .contact--post { top: 331px; }
  .contact__icon {
    flex: none;
    width: 41px; height: 41px;
  }
  .contact__lines { margin: 0; }

  /* back */
  .card--back svg { position: absolute; left: 0; top: 0; }
  .back-name {
    font-family: "Source Sans 3", sans-serif;
    font-weight: 700;
    font-size: 31px;
    letter-spacing: 0.6px;
    fill: var(--brand-blue);
  }
  .back-tagline {
    font-family: "Source Sans 3", sans-serif;
    font-weight: 700;
    font-size: 14px;
    fill: var(--brand-blue);
  }
</style>
</head>
<body>
<main class="stage">

  <section class="card card--front" aria-label="Business card front">
    <div class="side-band">
      <svg width="179" height="456" viewBox="0 0 179 456">
        <line x1="63" y1="59" x2="63" y2="406" stroke="#fff" stroke-width="1.5"/>
        <line x1="110" y1="59" x2="110" y2="406" stroke="#fff" stroke-width="1.5"/>
        <text class="band-name" transform="translate(95 278) rotate(-90)">TAMBERLINE BREAKER</text>
        <text class="band-tagline" transform="translate(118 268) rotate(-90)">A Voltren Assemblies, Inc. Company</text>
        <rect x="55" y="300" width="64" height="64" fill="#fff"/>
      </svg>
    </div>

    <div class="person">
      <h1 class="person__name">Darren Holloway</h1>
      <p class="person__title">Managing Director</p>
    </div>

    <div class="contact contact--phone">
      <svg class="contact__icon" viewBox="0 0 41 41" aria-hidden="true">
        <circle cx="20.5" cy="20.5" r="20.5" fill="var(--brand-blue)"/>
        <path d="M20.5 11c-4 0-6.5 3-6.5 6.8v4.7l-2 3h17l-2-3v-4.7c0-3.8-2.5-6.8-6.5-6.8z M18 27.5a2.5 2.5 0 0 0 5 0z" fill="#fff"/>
      </svg>
      <p class="contact__lines">(555) 014-2290</p>
    </div>

    <div class="contact contact--web">
      <svg class="contact__icon" viewBox="0 0 41 41" aria-hidden="true">
        <circle cx="20.5" cy="20.5" r="20.5" fill="var(--brand-blue)"/>
        <rect x="11" y="12" width="19" height="15" rx="1.5" fill="none" stroke="#fff" stroke-width="1.6"/>
        <line x1="11" y1="16" x2="30" y2="16" stroke="#fff" stroke-width="1.6"/>
        <circle cx="28" cy="26" r="4" fill="#fff"/>
        <path d="M26.2 26l1.3 1.3 2.3-2.5" fill="none" stroke="var(--brand-blue)" stroke-width="1.2"/>
      </svg>
      <p class="contact__lines">darren@tamberlinebreaker-example.com<br>www.tamberlinebreaker-example.com</p>
    </div>

    <div class="contact contact--post">
      <svg class="contact__icon" viewBox="0 0 41 41" aria-hidden="true">
        <circle cx="20.5" cy="20.5" r="20.5" fill="var(--brand-blue)"/>
        <path d="M24 10a4.5 4.5 0 0 0-4.5 4.5c0 3.4 4.5 8 4.5 8s4.5-4.6 4.5-8A4.5 4.5 0 0 0 24 10z" fill="#fff"/>
        <circle cx="24" cy="14.5" r="1.6" fill="var(--brand-blue)"/>
        <path d="M10 28l3-5h6l-1.5 5z M19 28l1.5-5h3l1 5z" fill="#fff"/>
      </svg>
      <p class="contact__lines">PO Box 418<br>Alderton, NC 28999</p>
    </div>
  </section>

  <section class="card card--back" aria-label="Business card back">
    <svg width="800" height="456" viewBox="0 0 800 456">
      <line x1="128" y1="190" x2="170" y2="190" stroke="var(--brand-blue)" stroke-width="2"/>
      <line x1="128" y1="261" x2="170" y2="261" stroke="var(--brand-blue)" stroke-width="2"/>
      <rect x="180" y="167" width="118" height="118" fill="var(--brand-blue)"/>
      <line x1="308" y1="190" x2="666" y2="190" stroke="var(--brand-blue)" stroke-width="2"/>
      <line x1="308" y1="261" x2="666" y2="261" stroke="var(--brand-blue)" stroke-width="2"/>
      <text class="back-name" x="487" y="237" text-anchor="middle">TAMBERLINE BREAKER</text>
      <text class="back-tagline" x="487" y="280" text-anchor="middle">A Voltren Assemblies, Inc. Company</text>
    </svg>
  </section>

</main>
</body>
</html>
```